Real Estate Business Cards

Looking for a clean, sharp and professional look for our Real Estate investment Fund that invests in Multi Family Apartment buildings.

Target Market(s)

Real Estate Fund

Industry/Entity Type

Real Estate

Contact Information for Business Card

Company Description: Real Estate Investment Fund
Company Name: KRV Holdings
Name: Marcus Tovell
Cell: (917) 482-0957
Email: marcus@krvholdings-example.com
Website: www.krvholdings-example.com
Address: 148, 7th Street, Brooklyn NY 11217

Colors

Designer to choose colors to be used in the design.

Requirements
Nice to have
• Colors to match logo

```html
<!DOCTYPE html>
<html lang="en">
<head>
<meta charset="utf-8">
<title>KRV Holdings – Business Cards</title>
<link href="https://fonts.googleapis.com/css2?family=Cormorant+Garamond:wght@500&family=Open+Sans:wght@400;600;700&display=swap" rel="stylesheet">
<style>
  :root {
    --bg-top: #a3a3a3;
    --bg-bottom: #d6d6d6;
    --brand-blue: #126aa0;
    --brand-blue-deep: #0f5784;
    --ink: #3a3a3a;
    --ink-soft: #5a5a5a;
    --paper: #ffffff;
    --paper-shade: #ececec;
  }
  * { box-sizing: border-box; margin: 0; padding: 0; }
  html, body { width: 1200px; height: 900px; overflow: hidden; }
  body {
    background: linear-gradient(180deg, var(--bg-top), var(--bg-bottom));
    font-family: "Open Sans", Arial, sans-serif;
    position: relative;
  }
  .card {
    position: absolute;
    width: 525px;
    height: 300px;
    box-shadow: 0 10px 24px rgba(0,0,0,0.28);
  }
  /* Front */
  .card--front {
    left: 70px; top: 110px;
    background: linear-gradient(160deg, var(--brand-blue-deep), var(--brand-blue));
    color: var(--paper);
  }
  .front-brand {
    position: absolute;
    left: 0; right: 0; top: 118px;
    display: flex; align-items: center; justify-content: center; gap: 16px;
  }
  .brand-square {
    width: 34px; height: 34px;
    border: 3px solid currentColor;
  }
  .brand-name {
    font-family: "Cormorant Garamond", Georgia, serif;
    font-weight: 500;
    font-size: 34px;
    letter-spacing: 3px;
    text-transform: uppercase;
  }
  .front-tagline {
    position: absolute;
    left: 0; right: 0; top: 200px;
    text-align: center;
    font-size: 13px;
    letter-spacing: 2.5px;
  }
  /* Back */
  .card--back {
    left: 605px; top: 490px;
    background: linear-gradient(200deg, var(--paper-shade) 0%, var(--paper) 55%);
    color: var(--ink);
  }
  .back-person {
    position: absolute;
    right: 34px; top: 34px;
    text-align: right;
  }
  .person-name {
    font-weight: 700;
    font-size: 20px;
    color: var(--brand-blue);
    text-transform: uppercase;
  }
  .person-title {
    font-size: 12px;
    letter-spacing: 1px;
    color: var(--ink-soft);
    text-transform: uppercase;
  }
  .back-brand {
    position: absolute;
    left: 34px; top: 34px;
    display: flex; align-items: center; gap: 10px;
    color: var(--brand-blue);
  }
  .back-brand .brand-square { width: 26px; height: 26px; }
  .back-brand .brand-name { font-size: 26px; letter-spacing: 2px; }
  .contact {
    position: absolute;
    left: 34px; bottom: 30px;
    font-size: 13px;
    line-height: 1.5;
    color: var(--ink);
    list-style: none;
  }
  .contact li { display: flex; align-items: center; gap: 8px; }
  .contact .address { padding-left: 0; }
  .contact svg { width: 13px; height: 13px; flex: none; }
</style>
</head>
<body>
  <section class="card card--front" aria-label="Business card front">
    <div class="front-brand">
      <span class="brand-square"></span>
      <span class="brand-name">KRV Holdings</span>
    </div>
    <p class="front-tagline">Real Estate Investment Fund</p>
  </section>

  <section class="card card--back" aria-label="Business card back">
    <div class="back-brand">
      <span class="brand-square"></span>
      <span class="brand-name">KRV Holdings</span>
    </div>
    <div class="back-person">
      <p class="person-name">Marcus Tovell</p>
      <p class="person-title">Realtor</p>
    </div>
    <ul class="contact">
      <li class="address">148, 7th Street</li>
      <li class="address">Brooklyn NY 11217</li>
      <li>
        <svg viewBox="0 0 14 14" aria-hidden="true"><rect x="3.5" y="1" width="7" height="12" rx="1.2" fill="none" stroke="#126aa0" stroke-width="1.4"/><line x1="6" y1="11" x2="8" y2="11" stroke="#126aa0" stroke-width="1.2"/></svg>
        (917) 482-0957
      </li>
      <li>
        <svg viewBox="0 0 14 14" aria-hidden="true"><rect x="1" y="3" width="12" height="8" fill="none" stroke="#126aa0" stroke-width="1.4"/><polyline points="1,3 7,8 13,3" fill="none" stroke="#126aa0" stroke-width="1.4"/></svg>
        marcus@krvholdings-example.com
      </li>
      <li>
        <svg viewBox="0 0 14 14" aria-hidden="true"><circle cx="7" cy="7" r="5.8" fill="none" stroke="#126aa0" stroke-width="1.3"/><ellipse cx="7" cy="7" rx="2.6" ry="5.8" fill="none" stroke="#126aa0" stroke-width="1.1"/><line x1="1.2" y1="7" x2="12.8" y2="7" stroke="#126aa0" stroke-width="1.1"/></svg>
        www.krvholdings-example.com
      </li>
    </ul>
  </section>
</body>
</html>
```